Birchline Flooring Supply

Basic one-sided business card design using the attached logo. Vintage americana theme. Font is modified Arial Nova Cond, but anything that coordinates can be used

```html
<!DOCTYPE html>
<html lang="en">
<head>
<meta charset="utf-8">
<title>Birchline Flooring Supply – Business Card</title>
<link href="https://fonts.googleapis.com/css2?family=Montserrat:wght@400;500;700&display=swap" rel="stylesheet">
<style>
  :root {
    --bg: #3a3b3d;
    --card-white: #ffffff;
    --card-black: #1b1b1b;
    --gold: #b59a74;
    --ink: #1f1f1f;
    --light: #f4f1ec;
  }
  * { box-sizing: border-box; margin: 0; padding: 0; }
  html, body { width: 1200px; height: 1200px; overflow: hidden; }
  body {
    background: var(--bg);
    font-family: "Montserrat", Arial, sans-serif;
    position: relative;
  }
  .card {
    position: absolute;
    left: 150px;
    width: 900px;
    height: 514px;
    border-radius: 30px;
    overflow: hidden;
    box-shadow: 0 14px 30px rgba(0,0,0,0.35);
  }
  .card--front { top: 50px; background: var(--card-white); }
  .card--back { top: 636px; background: var(--card-black); }

  .card__band { position: absolute; inset: 0; width: 100%; height: 100%; }

  .contact {
    position: absolute;
    left: 70px;
    top: 190px;
    color: var(--ink);
  }
  .contact__name {
    font-size: 50px;
    font-weight: 700;
    color: var(--gold);
    letter-spacing: 0.5px;
    line-height: 1;
  }
  .contact__position {
    font-size: 22px;
    font-weight: 500;
    margin-top: 4px;
    letter-spacing: 0.5px;
  }
  .contact__list { list-style: none; margin-top: 14px; }
  .contact__item {
    display: flex;
    align-items: flex-start;
    gap: 16px;
    font-size: 22px;
    line-height: 1.2;
    margin-bottom: 6px;
  }
  .contact__icon { width: 26px; height: 26px; flex: none; margin-top: 2px; }

  .wordmark {
    position: absolute;
    font-weight: 700;
    text-transform: uppercase;
    text-align: center;
    line-height: 1.15;
  }
  .wordmark--front {
    right: 70px;
    top: 100px;
    width: 330px;
    font-size: 30px;
    color: var(--ink);
  }
  .wordmark--back {
    left: 0; right: 0;
    top: 190px;
    font-size: 46px;
    color: var(--gold);
    letter-spacing: 1px;
  }

  .website {
    position: absolute;
    right: 50px;
    top: 412px;
    font-size: 21px;
    color: var(--light);
    letter-spacing: 1px;
  }
</style>
</head>
<body>

<section class="card card--front" aria-label="Business card front">
  <svg class="card__band" viewBox="0 0 900 514" preserveAspectRatio="none" aria-hidden="true">
    <path d="M0 458 H480 C535 458 545 374 610 374 H900 V514 H0 Z" fill="var(--gold)"/>
    <path d="M0 468 H480 C543 468 553 384 618 384 H900 V514 H0 Z" fill="var(--card-black)"/>
  </svg>

  <div class="contact">
    <div class="contact__name">FULL NAME</div>
    <div class="contact__position">POSITION</div>
    <ul class="contact__list">
      <li class="contact__item">
        <svg class="contact__icon" viewBox="0 0 24 24" aria-hidden="true"><path fill="var(--gold)" d="M6.6 10.8a15.1 15.1 0 0 0 6.6 6.6l2.2-2.2c.3-.3.7-.4 1-.2 1.1.4 2.3.6 3.6.6.6 0 1 .4 1 1V20c0 .6-.4 1-1 1A17 17 0 0 1 3 4c0-.6.4-1 1-1h3.5c.6 0 1 .4 1 1 0 1.3.2 2.5.6 3.6.1.3 0 .7-.2 1z"/></svg>
        <span>(000) 000 0000</span>
      </li>
      <li class="contact__item">
        <svg class="contact__icon" viewBox="0 0 24 24" aria-hidden="true"><path fill="var(--gold)" d="M2 5h20v14H2z"/><path fill="none" stroke="#fff" stroke-width="1.6" d="M2 5l10 8 10-8M2 19l7-7M22 19l-7-7"/></svg>
        <span>email@company.com</span>
      </li>
      <li class="contact__item">
        <svg class="contact__icon" viewBox="0 0 24 24" aria-hidden="true"><path fill="var(--gold)" d="M12 2a7 7 0 0 0-7 7c0 5 7 13 7 13s7-8 7-13a7 7 0 0 0-7-7zm0 10a3 3 0 1 1 0-6 3 3 0 0 1 0 6z"/></svg>
        <span>123 Name Street, 000<br>Your City, 00000-000</span>
      </li>
    </ul>
  </div>

  <div class="wordmark wordmark--front">Birchline<br>Flooring Supply</div>

  <div class="website">www.company.com</div>
</section>

<section class="card card--back" aria-label="Business card back">
  <div class="wordmark wordmark--back">Birchline<br>Flooring Supply</div>
</section>

</body>
</html>
```